Re-Branding

I would like a new "brand" which will incorporate my new photo. I do title insurance in California for Harborline Deed Assurance Corp. Could be used on business cards or flyers.

Target Market(s)

Real Estate Professionals, Attorneys, Mortgage Companies and Banks.

Contact Information for Business Card

High Gloss

Requirements
Must have
• My photo, my logo and my contact information.
Nice to have
• background that is appealing to clients
Should not have
• home email address

```html
<!DOCTYPE html>
<html lang="en">
<head>
<meta charset="utf-8">
<title>Dana Whitfield – Business Card</title>
<link href="https://fonts.googleapis.com/css2?family=Cinzel:wght@600&family=Arimo:wght@400&display=swap" rel="stylesheet">
<style>
  :root{
    --stage:#e4e5e7;
    --paper:#ffffff;
    --navy:#1f2d6b;
    --navy-deep:#142057;
    --navy-light:#2c3d86;
    --green:#1f7a3c;
    --ink:#1c2450;
    --portrait-a:#e9ecea;
    --portrait-b:#2f9a62;
  }
  *{margin:0;padding:0;box-sizing:border-box}
  html,body{width:1200px;height:900px;overflow:hidden}
  body{background:var(--stage);position:relative;font-family:"Arimo",Arial,sans-serif}
  .card{
    position:absolute;top:80px;width:420px;height:740px;border-radius:28px;
    overflow:hidden;background:var(--paper);
    box-shadow:0 10px 30px rgba(0,0,0,.18);
  }
  .card--front{left:150px}
  .card--back{left:630px}

  .front-heading{position:absolute;top:70px;left:0;right:0;text-align:center}
  .holder-name{font-family:"Cinzel",Georgia,serif;font-weight:600;font-size:38px;letter-spacing:2px;color:var(--green)}
  .holder-role{font-size:18px;color:var(--ink);margin-top:6px;letter-spacing:.3px}
  .portrait{
    position:absolute;left:30px;right:0;bottom:0;height:560px;
    background:linear-gradient(180deg,var(--portrait-a) 0%,#d9c7a4 30%,var(--portrait-b) 58%,#1d8a52 100%);
    border-top-left-radius:200px 160px;
  }

  .back-panel{
    position:absolute;left:0;right:0;top:0;height:600px;
    background:linear-gradient(160deg,var(--navy-light) 0%,var(--navy) 50%,var(--navy-deep) 100%);
    border-bottom:5px solid var(--green);
    color:#fff;text-align:center;
  }
  .back-name{font-family:"Cinzel",Georgia,serif;font-weight:600;font-size:38px;letter-spacing:2px;margin-top:70px}
  .back-role{font-size:18px;margin-top:6px;letter-spacing:.3px}
  .divider{width:28px;height:3px;background:#fff;margin:38px auto}
  .contact-item{margin-bottom:34px}
  .contact-icon{width:22px;height:22px;display:block;margin:0 auto 10px}
  .contact-text{font-size:21px;letter-spacing:.4px}

  .brand{
    position:absolute;left:0;right:0;bottom:0;height:135px;
    display:flex;align-items:center;justify-content:center;gap:14px;
  }
  .brand-dot{width:40px;height:40px;border-radius:50%;background:var(--navy);flex:none}
  .brand-name{font-size:22px;line-height:1.2;color:var(--navy);max-width:260px}
</style>
</head>
<body>
  <section class="card card--front">
    <header class="front-heading">
      <h1 class="holder-name">DANA WHITFIELD</h1>
      <p class="holder-role">Account Executive | Vice President</p>
    </header>
    <div class="portrait" role="img" aria-label="Portrait photo of the account executive in a green top"></div>
  </section>

  <section class="card card--back">
    <div class="back-panel">
      <h2 class="back-name">DANA WHITFIELD</h2>
      <p class="back-role">Account Executive | Vice President</p>
      <div class="divider"></div>
      <div class="contact-item">
        <svg class="contact-icon" viewBox="0 0 22 22" aria-hidden="true"><circle cx="11" cy="11" r="11" fill="#fff"/><path d="M7 6.5l2 0 1 3-1.3 1a6 6 0 0 0 3 3l1-1.3 3 1v2a1.3 1.3 0 0 1-1.4 1.2A9 9 0 0 1 5.8 8a1.3 1.3 0 0 1 1.2-1.5z" fill="var(--navy)"/></svg>
        <p class="contact-text">909-555-0142</p>
      </div>
      <div class="contact-item">
        <svg class="contact-icon" viewBox="0 0 22 22" aria-hidden="true"><circle cx="11" cy="11" r="11" fill="#fff"/><rect x="5.5" y="7" width="11" height="8" rx="1" fill="var(--navy)"/><path d="M5.8 7.4L11 11.5l5.2-4.1" stroke="#fff" stroke-width="1" fill="none"/></svg>
        <p class="contact-text">DWhitfield@hdac.com</p>
      </div>
      <div class="contact-item">
        <svg class="contact-icon" viewBox="0 0 22 22" aria-hidden="true"><circle cx="11" cy="11" r="11" fill="#fff"/><path d="M9.5 12.5l3-3M8.6 10.4l-1.5 1.5a2.1 2.1 0 0 0 3 3l1.5-1.5M13.4 11.6l1.5-1.5a2.1 2.1 0 0 0-3-3l-1.5 1.5" stroke="var(--navy)" stroke-width="1.6" fill="none" stroke-linecap="round"/></svg>
        <p class="contact-text">Dana.HarborlineIE.com</p>
      </div>
      <div class="divider" style="margin-top:8px"></div>
    </div>
    <div class="brand">
      <span class="brand-dot"></span>
      <p class="brand-name">Harborline Deed Assurance Corp.</p>
    </div>
  </section>
</body>
</html>
```